Dietitian needs awesome business card

I need a contemporary design that's eye catching but professional.
My card is to given to doctors, specialists and patients alike.
I manage patients with chronic diseases
I have uploaded my logo and current business card, I would also like the other Registered Clinical Nutritionist logo incorporated into the design

Target Market(s)

Doctors, specialists and patients

Industry/Entity Type

Healthcare

Contact Information for Business Card

www.brindlecovenutrition.com.au
Ph: 0427 516 903
Fax: 6482 7315
email: marcus.k.wellfare@quorvamail.com
Space on the back of the card with: Appointment date, Appointment time and appointment location

Font styles to use
Serif

Colors
fbee3e
876aae
ffc214

Requirements
Must have
• My Logo
• Registered Clinical Nutritionist Logo
• My 4 locations - Fernhollow Medical Centre, North Kelby Health, Ashcourt Medical, Pinebrook Doctors Surgery
Nice to have
• I like the colours in my current business card

```html
<!DOCTYPE html>
<html lang="en">
<head>
<meta charset="utf-8">
<title>Brindlecove Nutrition &amp; Dietetics – Business Card</title>
<link rel="stylesheet" href="https://fonts.googleapis.com/css2?family=Source+Sans+3:wght@400;500&display=swap">
<style>
  :root{
    --backdrop:#3a3a3a;
    --card:#ffffff;
    --navy:#2a2f8f;
    --blue-left:#2674b9;
    --blue-right:#2b3587;
    --green:#3fb43b;
    --green-swoosh:#7cc242;
    --grey-text:#555555;
    --rule:#6a6a6a;
    --badge:#f47c20;
  }
  *{margin:0;padding:0;box-sizing:border-box;}
  html,body{width:1200px;height:1200px;overflow:hidden;}
  body{background:var(--backdrop);font-family:"Source Sans 3",sans-serif;position:relative;}
  .card{position:absolute;left:254px;width:691px;height:391px;background:var(--card);overflow:hidden;}
  .card--front{top:171px;}
  .card--back{top:638px;}
  .abs{position:absolute;line-height:1;white-space:nowrap;}

  /* front */
  .band{position:absolute;left:0;top:0;width:691px;height:391px;}
  .brand-mark{position:absolute;left:362px;top:52px;width:64px;height:64px;border-radius:50%;background:var(--green-swoosh);}
  .brand-name{right:27px;top:72px;font-size:42px;color:var(--navy);font-weight:400;}
  .brand-sub{right:27px;top:111px;font-size:19px;color:var(--navy);font-weight:400;}
  .holder-name{left:34px;top:169px;font-size:26px;color:var(--navy);}
  .holder-title{left:34px;top:197px;font-size:18px;color:var(--green);}
  .contact-list{position:absolute;left:0;top:0;list-style:none;}
  .contact-item{position:absolute;left:46px;display:flex;align-items:center;gap:6px;color:#fff;font-size:17.6px;line-height:1;white-space:nowrap;}
  .contact-item svg{width:16px;height:16px;flex:none;}
  .contact-item--phone{top:271px;}
  .contact-item--fax{top:294px;}
  .contact-item--mail{top:317px;}
  .contact-item--web{top:340px;}
  .credential-badge{position:absolute;left:511px;top:254px;width:118px;height:55px;background:var(--badge);border-radius:2px;}

  /* back */
  .centered{left:0;width:100%;text-align:center;}
  .back-name{top:31px;font-size:26px;color:var(--navy);}
  .back-address{top:61px;font-size:18px;color:var(--green);}
  .back-tel{top:84px;font-size:18px;color:var(--grey-text);}
  .back-fax{top:108px;font-size:18px;color:var(--grey-text);}
  .rule{position:absolute;left:72px;width:547px;height:1px;background:var(--rule);}
  .rule--top{top:177px;}
  .rule--bottom{top:241px;}
  .appt-label{top:188px;font-size:18px;color:var(--grey-text);}
  .field-label{top:247px;font-size:18px;color:var(--grey-text);transform:translateX(-50%);}
  .field-label--day{left:157px;}
  .field-label--month{left:346px;}
  .field-label--date{left:530px;}
  .time-slot{top:295px;font-size:18px;color:var(--grey-text);}
  .time-slot--am{left:253px;}
  .time-slot--pm{left:351px;}
  .time-slot span{display:inline-block;width:54px;border-bottom:1px solid var(--rule);margin-left:3px;}
  .notice{top:348px;font-size:15px;color:var(--grey-text);}
</style>
</head>
<body>

<section class="card card--front" aria-label="Card front">
  <svg class="band" viewBox="0 0 691 391" aria-hidden="true">
    <defs>
      <linearGradient id="bandFill" x1="0" y1="0" x2="1" y2="0">
        <stop offset="0" stop-color="#2674b9"/>
        <stop offset="1" stop-color="#2b3587"/>
      </linearGradient>
    </defs>
    <path d="M0,238 C180,232 330,248 440,305 C520,348 600,348 691,342 L691,391 L0,391 Z" fill="url(#bandFill)"/>
    <path d="M340,268 C430,322 500,342 560,340 C620,338 660,334 691,328 L691,340 C640,346 590,350 540,349 C470,346 420,318 340,268 Z" fill="var(--green-swoosh)"/>
    <path d="M340,268 C430,330 500,348 560,346" fill="none" stroke="#fff" stroke-width="3"/>
  </svg>

  <div class="brand-mark" aria-hidden="true"></div>
  <div class="abs brand-name">Brindlecove</div>
  <div class="abs brand-sub">Nutrition &amp; Dietetics</div>

  <div class="abs holder-name">Marcus Kellaway</div>
  <div class="abs holder-title">Registered Clinical Nutritionist, Nutritionist and Chef</div>

  <ul class="contact-list">
    <li class="contact-item contact-item--phone">
      <svg viewBox="0 0 16 16"><path d="M1 6 C3 2 13 2 15 6 L12 7 L11 5 C9 4.5 7 4.5 5 5 L4 7 Z" fill="#fff"/><rect x="3" y="8" width="10" height="6" rx="1" fill="#fff"/></svg>
      0427 516 930
    </li>
    <li class="contact-item contact-item--fax">
      <svg viewBox="0 0 16 16"><rect x="4" y="1" width="8" height="5" fill="#fff"/><rect x="1" y="6" width="14" height="6" rx="1" fill="#fff"/><rect x="4" y="10" width="8" height="5" fill="#fff" stroke="#2674b9"/></svg>
      Fax: 6482 7315
    </li>
    <li class="contact-item contact-item--mail">
      <svg viewBox="0 0 16 16"><rect x="1" y="3" width="14" height="10" fill="none" stroke="#fff" stroke-width="1.5"/><path d="M1 3 L8 9 L15 3 M1 13 L6 8 M15 13 L10 8" fill="none" stroke="#fff" stroke-width="1.5"/></svg>
      marcus.k.wellfare@quorvamail.com
    </li>
    <li class="contact-item contact-item--web">
      <svg viewBox="0 0 16 16" fill="none" stroke="#fff" stroke-width="1.2"><circle cx="8" cy="8" r="7"/><ellipse cx="8" cy="8" rx="3" ry="7"/><path d="M1 8 H15 M2.5 4.5 H13.5 M2.5 11.5 H13.5"/></svg>
      www.brindlecovenutrition.com.au
    </li>
  </ul>

  <div class="credential-badge" role="img" aria-label="Professional credential badge"></div>
</section>

<section class="card card--back" aria-label="Card back">
  <div class="abs centered back-name">Marcus Kellaway</div>
  <div class="abs centered back-address">Ashcourt Medical | 5/117 Harlow Road | Ashcourt Tasmania 7268</div>
  <div class="abs centered back-tel">Tel: 0427 516 903</div>
  <div class="abs centered back-fax">Fax: +613 6482 7315</div>

  <div class="rule rule--top"></div>
  <div class="abs centered appt-label">Has an Appoinment On</div>
  <div class="rule rule--bottom"></div>

  <div class="abs field-label field-label--day">DAY</div>
  <div class="abs field-label field-label--month">MONTH</div>
  <div class="abs field-label field-label--date">DATE</div>

  <div class="abs time-slot time-slot--am">AM.<span></span></div>
  <div class="abs time-slot time-slot--pm">PM.<span></span></div>

  <div class="abs centered notice">If unable to keep appointment, please give 24-hour notice</div>
</section>

</body>
</html>
```